Looking for a cool, modern Cannabis Jar Label

I want you to come up with a better, modern look for a label.

I need it sized to 4” x 3” - I plan to print directly to label printer.

I want you to use Photoshop and deliver me a layered PSD file that I can edit and modify the information as needed..

The label information will need to include places for:
(1) Strain Name - most important part of label - larger font size than rest - example Marlow Frost, KTV #7, Copperleaf Haze
(2) Pricing - for Gram, 1/8, 1/4, 1/2. and Ounce
(3) Strain Designation (Hybrid, Indica or Sativa) - maybe color coded, different color for Indica v. Sativa, just an idea
(4) THC and CBD percentages - for example 23% THC and 0.05% CBD
(5) Farm name - a place where we can add the name/logo of the business that produced the product. example - Bramwell Farms

I have attached a simple mockup showing the information.

I have also attached a few samples of labels we like to give you an idea of the look and feel we are going for.

I am wanting a very clean, modern, classy, readable look.The font will use is Gotham Font.

HI Everyone! Thank you for all of your designs. I am requesting an extension because I need more time to give adequate feedback to the designers. Thank you for your participation and all of your efforts! I will be making a decision soon!

• Gotham Font

Designer to choose colors to be used in the design.

• Thank you for your designs. I am sorry i have been slow in providing feedback, things have been really busy around here!
• I wanted to give some group general feedback. After reviewing all of the designs, there is a common theme among all of the designs that I would like to see changed.
• I would like to see the per gram pricing more prominent on the label. This is what most people are looking for when they are purchasing the product. So I would like to see this stand out from the other pricing tiers. As I think about it, they don't all need to be grouped together in a line. You could have the Per Gram pricing front and center some where and then the other pricing tiers grouped together somewhere else on the label.
• This is the order of importance of items on the label. Items at the the top of the list should be bigger than those below it.
• 1. Strain name
• 2. Pricing - being per gram the most important of all prices
• 3. THC/CBD percentages
• 4. Strain Type (indica, sativa, hybrid)
• 5. Farm name/logo
• When laying out these labels, they will be going on rounded jars and they will be on display. Think of jars with fancy labels in a candy store. They need to be eye catchy, appealing, but easy read.
• Thank you for all of your hard work, everyone is doing a great job.
• Best,
• Nadia

```html
<!DOCTYPE html>
<html lang="en">
<head>
<meta charset="utf-8">
<title>Amber Creek Chill – Jar Label</title>
<link rel="stylesheet" href="https://fonts.googleapis.com/css2?family=Montserrat:wght@300;400&display=swap">
<style>
  :root {
    --frame: #cf9bfb;
    --panel: #ffffff;
    --header: #9156fd;
    --ink: #2c0f6b;
    --title-outline: #3a2466;
    --tier-1: #ecdcff;
    --tier-2: #dcb9fc;
    --tier-3: #c89cfd;
    --tier-4: #b07ffd;
    --tier-5: #9a61fd;
    --type-main: #f8e6a6;
    --type-mid: #fbf1c9;
    --type-light: #fbf7e4;
    --leaf: #e2c400;
    --pill: #a565fd;
    --pill-cap: #e7d6ff;
  }
  * { box-sizing: border-box; margin: 0; padding: 0; }
  html, body { width: 1200px; height: 917px; overflow: hidden; background: var(--frame); }
  body { font-family: "Montserrat", sans-serif; color: var(--ink); }

  .label {
    position: absolute; left: 46px; top: 45px;
    width: 1107px; height: 824px;
    background: var(--panel); overflow: hidden;
  }

  .header {
    position: absolute; left: 0; top: 0; width: 100%; height: 306px;
    background: var(--header);
  }
  .leaf-accent {
    position: absolute; top: 0; width: 200px; height: 190px;
    background: radial-gradient(ellipse at 50% 45%, var(--leaf) 0%, rgba(226,196,0,0.55) 40%, rgba(226,196,0,0) 70%);
  }
  .leaf-accent.left { left: 0; }
  .leaf-accent.right { right: 0; }
  .strain-name {
    position: absolute; left: 0; top: 20px; width: 100%;
    text-align: center; font-weight: 300; font-size: 124px; line-height: 134px;
    color: #fff; -webkit-text-stroke: 1.5px var(--title-outline);
  }

  .price-row {
    position: absolute; left: 0; top: 309px; width: 100%; height: 118px;
    display: flex;
  }
  .price-tier { position: relative; height: 100%; }
  .price-tier .unit {
    position: absolute; right: 10px; top: 6px; font-size: 28px; font-weight: 300;
  }
  .price-tier .amount {
    position: absolute; left: 0; right: 0; top: 36px; text-align: center;
    font-size: 64px; font-weight: 300; line-height: 1;
  }
  .tier-gram  { width: 213px; background: var(--tier-1); }
  .tier-eighth{ width: 227px; background: var(--tier-2); }
  .tier-quarter{ width: 228px; background: var(--tier-3); }
  .tier-half  { width: 227px; background: var(--tier-4); }
  .tier-ounce { width: 212px; background: var(--tier-5); }

  .strain-type {
    position: absolute; left: 0; top: 472px; width: 100%; height: 120px;
    display: flex;
  }
  .type-main { width: 668px; background: var(--type-main); position: relative; }
  .type-mid { width: 225px; background: var(--type-mid); }
  .type-light { flex: 1; background: var(--type-light); }
  .type-name {
    position: absolute; left: 143px; top: 6px;
    font-size: 96px; font-weight: 300; line-height: 110px;
  }

  .potency {
    position: absolute; top: 628px; width: 115px; height: 196px;
    background: var(--pill); border-radius: 58px 58px 0 0;
  }
  .potency.thc { left: 150px; }
  .potency.cbd { left: 357px; }
  .potency .value {
    width: 115px; height: 115px; border-radius: 50%; background: var(--pill-cap);
    display: flex; align-items: center; justify-content: center;
    font-size: 40px; font-weight: 300;
  }
  .potency .name {
    position: absolute; left: 0; right: 0; top: 135px; text-align: center;
    font-size: 42px; font-weight: 300;
  }

  .farm {
    position: absolute; left: 598px; top: 627px; height: 132px;
    display: flex; align-items: center; gap: 26px;
  }
  .farm-mark { width: 132px; height: 132px; border: 3px solid var(--ink); border-radius: 50%; }
  .farm-name { font-size: 44px; font-weight: 400; line-height: 1.05; color: var(--ink); }
</style>
</head>
<body>
  <main class="label">
    <header class="header">
      <div class="leaf-accent left" role="img" aria-label="Golden cannabis leaf decoration"></div>
      <div class="leaf-accent right" role="img" aria-label="Golden cannabis leaf decoration"></div>
      <h1 class="strain-name">Amber<br>Creek Chill</h1>
    </header>

    <section class="price-row">
      <div class="price-tier tier-gram"><span class="unit">g.</span><span class="amount">$10</span></div>
      <div class="price-tier tier-eighth"><span class="unit">1/8</span><span class="amount">$35</span></div>
      <div class="price-tier tier-quarter"><span class="unit">1/4</span><span class="amount">$70</span></div>
      <div class="price-tier tier-half"><span class="unit">1/2</span><span class="amount">$140</span></div>
      <div class="price-tier tier-ounce"><span class="unit">Oz</span><span class="amount">$280</span></div>
    </section>

    <section class="strain-type">
      <div class="type-main"><span class="type-name">Indica</span></div>
      <div class="type-mid"></div>
      <div class="type-light"></div>
    </section>

    <div class="potency thc"><div class="value">28%</div><div class="name">THC</div></div>
    <div class="potency cbd"><div class="value">2%</div><div class="name">CBD</div></div>

    <div class="farm">
      <div class="farm-mark"></div>
      <div class="farm-name">Bramwell<br>Farms</div>
    </div>
  </main>
</body>
</html>
```